BrivaTrek Freight Services Business cards

Would like a very unique design catchy but professional for business cards. Please use log provided.Marlon WellsCeo and Founder TransCon Logistix Solutions1-888-913-3225mwells@tlsolutionsus.comwww.bfservicesco.com

```html
<!DOCTYPE html>
<html lang="en">
<head>
<meta charset="utf-8">
<title>BrivaTrek Freight Services – Business Cards</title>
<link rel="stylesheet" href="https://fonts.googleapis.com/css2?family=Open+Sans:wght@400;600;700&display=swap">
<style>
  :root {
    --page-bg: #e9eaec;
    --brand-blue: #1a7bbf;
    --brand-blue-deep: #1565a3;
    --brand-red: #e3242b;
    --card-white: #ffffff;
    --front-mark: #dbe8f4;
    --shadow: rgba(0, 0, 0, 0.18);
  }
  * { box-sizing: border-box; margin: 0; padding: 0; }
  html, body {
    width: 1200px;
    height: 831px;
    overflow: hidden;
    background: var(--page-bg);
    font-family: "Open Sans", Arial, sans-serif;
  }
  .sheet {
    width: 1200px;
    height: 831px;
    display: flex;
    align-items: center;
    justify-content: center;
    gap: 60px;
  }
  .card {
    position: relative;
    width: 520px;
    height: 300px;
    overflow: hidden;
    box-shadow: 0 10px 24px var(--shadow);
  }

  /* Front */
  .card-front {
    background: var(--brand-blue);
    display: flex;
    align-items: center;
    justify-content: center;
  }
  .front-brand {
    display: flex;
    align-items: center;
    gap: 14px;
    color: var(--front-mark);
    font-weight: 700;
    font-size: 30px;
    letter-spacing: 0.5px;
  }
  .front-brand .brand-square {
    width: 34px;
    height: 34px;
    background: var(--front-mark);
  }

  /* Back */
  .card-back { background: var(--card-white); }
  .back-band {
    position: absolute;
    left: 0;
    right: 0;
    bottom: 0;
    height: 118px;
    background: linear-gradient(180deg, var(--brand-blue) 0%, var(--brand-blue-deep) 100%);
  }
  .person {
    position: absolute;
    left: 36px;
    top: 30px;
  }
  .person-name {
    font-size: 21px;
    font-weight: 400;
    letter-spacing: 0.3px;
    color: var(--brand-blue);
    line-height: 1.1;
  }
  .person-name .surname { color: var(--brand-red); }
  .person-title {
    font-size: 13px;
    color: var(--brand-red);
    margin-top: 2px;
  }
  .contact {
    position: absolute;
    left: 36px;
    top: 118px;
    list-style: none;
    font-size: 14px;
    color: var(--brand-blue);
    line-height: 1.45;
  }
  .contact li { display: flex; align-items: center; gap: 8px; }
  .contact svg { width: 12px; height: 12px; fill: var(--brand-red); flex: none; }
  .company {
    position: absolute;
    right: 26px;
    top: 118px;
    display: flex;
    align-items: center;
    gap: 8px;
    color: var(--brand-blue);
    font-weight: 700;
    font-size: 15px;
  }
  .company .brand-square {
    width: 16px;
    height: 16px;
    background: var(--brand-red);
  }
  .website {
    position: absolute;
    right: 30px;
    bottom: 22px;
    color: var(--card-white);
    font-size: 16px;
    letter-spacing: 2px;
  }
</style>
</head>
<body>
<main class="sheet">
  <section class="card card-front" aria-label="Business card front">
    <div class="front-brand"><span class="brand-square"></span>BrivaTrek</div>
  </section>

  <section class="card card-back" aria-label="Business card back">
    <div class="back-band" role="img" aria-label="Blue and red wave ornament along the lower edge"></div>

    <div class="person">
      <p class="person-name">DUSTIN <span class="surname">HARROW</span></p>
      <p class="person-title">Ceo and Founder</p>
    </div>

    <ul class="contact">
      <li>
        <svg viewBox="0 0 24 24" aria-hidden="true"><path d="M6.6 10.8a15.1 15.1 0 0 0 6.6 6.6l2.2-2.2a1 1 0 0 1 1-.25 11.4 11.4 0 0 0 3.6.57 1 1 0 0 1 1 1V20a1 1 0 0 1-1 1A17 17 0 0 1 3 4a1 1 0 0 1 1-1h3.5a1 1 0 0 1 1 1c0 1.25.2 2.45.57 3.57a1 1 0 0 1-.25 1z"/></svg>
        1-888-472-6081
      </li>
      <li>
        <svg viewBox="0 0 24 24" aria-hidden="true"><path d="M2 5h20v14H2z M2 5l10 8 10-8" fill="var(--brand-red)" stroke="#fff" stroke-width="1.5"/></svg>
        dharrow@bfservicesco.com
      </li>
    </ul>

    <div class="company"><span class="brand-square"></span>BrivaTrek Freight Services</div>

    <p class="website">www.bfservicesco.com</p>
  </section>
</main>
</body>
</html>
```